plumbers buisness card

A buisness card for a plumbing buisness
needs to have a water theme with navy blue, light blue and white
with an image of either a water drop, pipes, tools or something relating to plumbing and incorperating my buisness name as a logo

"Kesterly Plumbing" is the words that need to stand out with "& gasfitting" to be smaller
Updates

spelling error on brief, "maintenance"
and also could you include my email m_kesterly@mailnest.com.au

Industry/Entity Type

Plumbing

Contact Information for Business Card

Kesterly Plumbing & Gasfitting

marcus kesterly
0493612085

specialising in
-new homes
-maitenance
-renovations

license no.
-73804

```html
<!DOCTYPE html>
<html lang="en">
<head>
<meta charset="utf-8">
<title>Kesterly Plumbing &amp; Gasfitting — Business Card</title>
<link rel="stylesheet" href="https://fonts.googleapis.com/css2?family=Michroma&display=swap">
<style>
  :root {
    --backdrop: #e6e8eb;
    --card-white: #ffffff;
    --brand-blue: #1b84c6;
    --brand-blue-light: #3fa3e0;
    --brand-navy: #0d4f8a;
    --ink: #4f5359;
    --card-shadow: 0 10px 30px rgba(20, 40, 70, 0.18);
  }
  * { box-sizing: border-box; margin: 0; padding: 0; }
  html, body {
    width: 1200px;
    height: 800px;
    overflow: hidden;
    background: var(--backdrop);
    font-family: "Michroma", "Arial", sans-serif;
  }
  .canvas {
    width: 1200px;
    height: 800px;
    display: flex;
    align-items: center;
    justify-content: center;
    gap: 40px;
  }
  .card {
    position: relative;
    width: 560px;
    height: 342px;
    border-radius: 4px;
    overflow: hidden;
    box-shadow: var(--card-shadow);
  }

  /* Brand name lockup */
  .brand {
    display: flex;
    align-items: center;
    gap: 14px;
    text-transform: uppercase;
  }
  .brand-square {
    width: 52px;
    height: 52px;
    border-radius: 8px;
    flex: none;
  }
  .brand-name {
    line-height: 1.05;
    letter-spacing: 0.5px;
  }
  .brand-name .primary { display: block; font-size: 24px; }
  .brand-name .secondary { display: block; font-size: 13px; margin-top: 3px; }

  /* Front */
  .card-front { background: var(--card-white); }
  .card-front .brand { position: absolute; left: 44px; top: 56px; }
  .card-front .brand-square { background: var(--brand-blue); }
  .card-front .brand-name { color: var(--brand-blue); }

  .contact {
    position: absolute;
    left: 44px;
    top: 168px;
    text-transform: uppercase;
  }
  .contact-name {
    color: var(--brand-blue);
    font-size: 18px;
    letter-spacing: 0.5px;
    margin-bottom: 8px;
  }
  .contact-line {
    color: var(--ink);
    font-size: 11.5px;
    letter-spacing: 0.6px;
    line-height: 1.55;
  }
  .contact-line .divider { margin: 0 8px; }

  .services {
    position: absolute;
    left: 44px;
    bottom: 44px;
    color: var(--brand-blue);
    font-size: 11.5px;
    letter-spacing: 0.6px;
    text-transform: uppercase;
  }
  .services .divider { color: var(--ink); margin: 0 6px; }

  .water-band {
    position: absolute;
    left: 0;
    right: 0;
    bottom: 0;
    height: 26px;
    background: linear-gradient(90deg, var(--brand-navy), var(--brand-blue) 45%, var(--brand-blue-light));
  }

  /* Back */
  .card-back {
    background: radial-gradient(ellipse at 40% 35%, var(--brand-blue-light), var(--brand-blue) 55%, var(--brand-navy));
  }
  .card-back .water-photo {
    position: absolute;
    inset: 0;
  }
  .card-back .brand {
    position: absolute;
    right: 46px;
    top: 50%;
    transform: translateY(-50%);
  }
  .card-back .brand-square { background: var(--card-white); width: 64px; height: 64px; }
  .card-back .brand-name { color: var(--card-white); }
  .card-back .brand-name .primary { font-size: 28px; }
  .card-back .brand-name .secondary { font-size: 15px; }
</style>
</head>
<body>
  <main class="canvas">
    <section class="card card-front" aria-label="Business card front">
      <div class="brand">
        <span class="brand-square" aria-hidden="true"></span>
        <span class="brand-name">
          <span class="primary">Kesterly Plumbing</span>
          <span class="secondary">&amp; Gasfitting</span>
        </span>
      </div>

      <div class="contact">
        <p class="contact-name">Marcus Kesterly</p>
        <p class="contact-line">0493612085<span class="divider">|</span>License No. 73804</p>
        <p class="contact-line">m_kesterly@mailnest.com.au</p>
      </div>

      <p class="services">
        New Homes<span class="divider">|</span>Maintenance<span class="divider">|</span>Renovations
      </p>

      <div class="water-band" role="img" aria-label="Blue band with water droplets"></div>
    </section>

    <section class="card card-back" aria-label="Business card back">
      <div class="water-photo" role="img" aria-label="Photograph of water droplets on blue glass"></div>
      <div class="brand">
        <span class="brand-square" aria-hidden="true"></span>
        <span class="brand-name">
          <span class="primary">Kesterly Plumbing</span>
          <span class="secondary">&amp; Gasfitting</span>
        </span>
      </div>
    </section>
  </main>
</body>
</html>
```